Branding for salad and dip containers - retail

we are trying to modernise our packaging design
the lids will be pre-printed (only with our logo) the design can be any shape, preferably not covering the whole top as we want the product to show
NO OTHER details are needed on the lid! Just the logo in bold modern design (using our existing logo and colours) fresh modern and bold
this is the container size we use
https://www.vessorix7.co.uk/acatalog/280ml-rectangular-clear-tamperproof-container-lid.html#SID=64
see images attached of some trials made that we don’t like
1) One has too many other details
2) The other has not utilised our brand and logo

Target Market(s)

Retail Customers

Industry/Entity Type

food

Requirements
Must have
• our current existing logo included
Nice to have
• i would like to see my logo rebranded in a modern sleek design ready to printed on container tops
Should not have
• none of the current add ons- just logo bold and modern

```html
<!DOCTYPE html>
<html lang="en">
<head>
<meta charset="utf-8">
<title>Fernbrook's lid label</title>
<link rel="stylesheet" href="https://fonts.googleapis.com/css2?family=Roboto+Condensed:wght@700&display=swap">
<style>
  :root {
    --page-bg: #ffffff;
    --red-light: #f0414a;
    --red-mid: #e01f29;
    --red-deep: #b5121b;
    --grey-light: #d9d9db;
    --grey-mid: #c4c4c6;
    --grey-deep: #a9a9ac;
    --brand-white: #ffffff;
    --disc-shade: #e6e6e8;
  }
  html, body {
    margin: 0;
    padding: 0;
    width: 849px;
    height: 1200px;
    overflow: hidden;
    background: var(--page-bg);
  }
  .canvas {
    width: 849px;
    height: 1200px;
    display: flex;
    align-items: center;
    justify-content: center;
  }
  .lid-label {
    width: 560px;
    height: 700px;
    display: block;
  }
  .lid-label__name {
    font-family: "Roboto Condensed", sans-serif;
    font-weight: 700;
    font-size: 74px;
    fill: var(--brand-white);
  }
</style>
</head>
<body>
  <main class="canvas">
    <svg class="lid-label" viewBox="0 0 560 700" xmlns="http://www.w3.org/2000/svg" aria-labelledby="label-title">
      <title id="label-title">Fernbrook's lid label</title>
      <defs>
        <clipPath id="label-shape">
          <rect x="0" y="0" width="560" height="700" rx="28" ry="28"/>
        </clipPath>
        <linearGradient id="grey-fill" x1="0" y1="0" x2="0" y2="1">
          <stop offset="0" stop-color="var(--grey-light)"/>
          <stop offset="0.6" stop-color="var(--grey-mid)"/>
          <stop offset="1" stop-color="var(--grey-deep)"/>
        </linearGradient>
        <radialGradient id="red-fill" cx="0.35" cy="0.25" r="0.9">
          <stop offset="0" stop-color="var(--red-light)"/>
          <stop offset="0.55" stop-color="var(--red-mid)"/>
          <stop offset="1" stop-color="var(--red-deep)"/>
        </radialGradient>
        <linearGradient id="gloss" x1="0" y1="0" x2="0" y2="1">
          <stop offset="0" stop-color="#ffffff" stop-opacity="0.28"/>
          <stop offset="1" stop-color="#ffffff" stop-opacity="0"/>
        </linearGradient>
        <radialGradient id="disc-fill" cx="0.4" cy="0.35" r="0.7">
          <stop offset="0.6" stop-color="var(--brand-white)"/>
          <stop offset="1" stop-color="var(--disc-shade)"/>
        </radialGradient>
        <filter id="soft-shadow" x="-30%" y="-30%" width="160%" height="160%">
          <feDropShadow dx="0" dy="6" stdDeviation="8" flood-color="#000" flood-opacity="0.3"/>
        </filter>
      </defs>
      <g clip-path="url(#label-shape)">
        <rect x="0" y="0" width="560" height="700" fill="url(#grey-fill)"/>
        <path d="M0 0 H560 V245 A280 280 0 0 1 0 245 Z" fill="url(#red-fill)" filter="url(#soft-shadow)"/>
        <path d="M0 0 H560 V120 Q280 190 0 150 Z" fill="url(#gloss)"/>
      </g>
      <text class="lid-label__name" x="280" y="108" text-anchor="middle" textLength="390" lengthAdjust="spacingAndGlyphs">Fernbrook's</text>
      <circle cx="280" cy="322" r="138" fill="url(#disc-fill)" filter="url(#soft-shadow)"/>
    </svg>
  </main>
</body>
</html>
```